BUILDERS MERCHANTS BUSINESS CARD

we need a business card for our long established builders merchants
we supply to both trade and diy
we offer an express delivery service
we would like TRV to standout as this our main trade mark logo
also our main colours are blue/white/yellow

Industry/Entity Type

Trade

Contact Information for Business Card

TRV BUILDERS MERCHANTS

SUPPLIERS OF ALL TYPES OF BUILDING MATERIALS

-SAND/CEMENT
-BRICKS/BLOCKS
-PLASTER/PLASTERBOARDS
-INSULATION
-FENCING/GARDEN PAVING
-PLUMBING
-ELECTRICAL
-EXPRESS DELIVERIES

EST OVER 30 YEARS

418 MARLOWE RISE
LONDON
NORWOOD
SE19 4XD

0208 5294861
0208 5392617
FAX 0208539 7283
EMAIL- TRVBUILDERSMERCHANTS@POSTVALE.CO.UK

```html
<!DOCTYPE html>
<html lang="en">
<head>
<meta charset="utf-8">
<title>TRV Builders Merchants – Business Card</title>
<link rel="stylesheet" href="https://fonts.googleapis.com/css2?family=Mulish:wght@400;700;900&display=swap">
<style>
  :root {
    --navy: #14265a;
    --yellow: #f2d11a;
    --white: #ffffff;
    --ink: #333333;
    --backdrop: #2a2a2a;
  }
  html, body {
    margin: 0;
    padding: 0;
    width: 1200px;
    height: 900px;
    overflow: hidden;
    background: var(--backdrop);
  }
  .canvas {
    position: relative;
    width: 1200px;
    height: 900px;
  }
  .card {
    position: absolute;
    left: 100px;
    top: 165px;
    width: 1000px;
    height: 571px;
    background: var(--white);
    border-radius: 6px;
    overflow: hidden;
    box-shadow: 0 20px 50px rgba(0,0,0,0.5);
    font-family: "Mulish", sans-serif;
  }
  .card-bands {
    position: absolute;
    inset: 0;
  }
  .brand {
    position: absolute;
    left: 70px;
    top: 70px;
  }
  .brand-name {
    margin: 0;
    color: var(--navy);
    font-weight: 900;
    font-size: 66px;
    line-height: 0.86;
    letter-spacing: -1px;
    text-transform: uppercase;
  }
  .brand-name span { display: block; }
  .est-tag {
    position: absolute;
    left: 185px;
    top: -6px;
    background: var(--yellow);
    color: var(--navy);
    font-weight: 700;
    font-size: 17px;
    padding: 2px 8px;
    white-space: nowrap;
  }
  .product-list {
    position: absolute;
    right: 60px;
    top: 118px;
    margin: 0;
    padding: 0;
    list-style: none;
    text-align: right;
    color: var(--ink);
    font-size: 21px;
    line-height: 33px;
    text-transform: uppercase;
  }
  .icon-rail {
    position: absolute;
    left: 0;
    top: 278px;
    width: 60px;
    height: 262px;
    background: var(--navy);
    border-radius: 0 14px 14px 0;
  }
  .icon-rail svg {
    position: absolute;
    left: 15px;
    width: 30px;
    height: 30px;
  }
  .contact-list {
    position: absolute;
    left: 95px;
    top: 288px;
    margin: 0;
    padding: 0;
    list-style: none;
    color: var(--ink);
    font-size: 21px;
    line-height: 45px;
  }
</style>
</head>
<body>
<div class="canvas">
  <div class="card">
    <svg class="card-bands" width="1000" height="571" viewBox="0 0 1000 571" aria-hidden="true">
      <polygon points="0,554 520,520 530,532 0,571" fill="var(--navy)"/>
      <path d="M560,530 Q575,512 600,510 L1000,470 L1000,500 L570,540 Z" fill="var(--yellow)"/>
    </svg>

    <div class="brand">
      <span class="est-tag">EST OVER 30 YEARS</span>
      <h1 class="brand-name"><span>TRV</span><span>Builders</span><span>Merchants</span></h1>
    </div>

    <ul class="product-list">
      <li>-Insulation</li>
      <li>-Sand/Cement</li>
      <li>-Bricks/Blocks</li>
      <li>-Plumbing/Electrical</li>
      <li>-Plaster/Plasterboards</li>
      <li>-Fencing/Garden Paving</li>
      <li>-Express Deliveries</li>
    </ul>

    <div class="icon-rail">
      <svg style="top:14px" viewBox="0 0 30 30" aria-label="Phone" role="img">
        <path d="M3 12 Q15 2 27 12 L24 15 L20 12 L20 9 Q15 7 10 9 L10 12 L6 15 Z" fill="var(--white)"/>
        <rect x="6" y="16" width="18" height="10" rx="2" fill="var(--white)"/>
      </svg>
      <svg style="top:62px" viewBox="0 0 30 30" aria-label="Phone" role="img">
        <path d="M3 12 Q15 2 27 12 L24 15 L20 12 L20 9 Q15 7 10 9 L10 12 L6 15 Z" fill="var(--white)"/>
        <rect x="6" y="16" width="18" height="10" rx="2" fill="var(--white)"/>
      </svg>
      <svg style="top:110px" viewBox="0 0 30 30" aria-label="Fax" role="img">
        <rect x="8" y="3" width="14" height="9" fill="var(--white)"/>
        <rect x="3" y="12" width="24" height="12" rx="2" fill="var(--white)"/>
        <rect x="9" y="20" width="12" height="7" fill="var(--white)" stroke="var(--navy)" stroke-width="1.5"/>
      </svg>
      <svg style="top:160px" viewBox="0 0 30 30" aria-label="Email" role="img">
        <rect x="3" y="7" width="24" height="16" fill="var(--white)"/>
        <polyline points="3,7 15,17 27,7" fill="none" stroke="var(--navy)" stroke-width="1.8"/>
      </svg>
      <svg style="top:210px" viewBox="0 0 30 30" aria-label="Location" role="img">
        <path d="M15 3 A8 8 0 0 1 23 11 Q23 17 15 27 Q7 17 7 11 A8 8 0 0 1 15 3 Z" fill="var(--white)"/>
        <circle cx="15" cy="11" r="3" fill="var(--navy)"/>
      </svg>
    </div>

    <ul class="contact-list">
      <li>0208 529 4861</li>
      <li>0208 539 2617</li>
      <li>0208 539 7283</li>
      <li>trvbuildersmerchants@postvale.co.uk</li>
      <li>418 Marlowe Rise,Norwood,London SE19 4XD</li>
    </ul>
  </div>
</div>
</body>
</html>
```